Dietitian clinic needs a business card design

We need a business card design for a new dietitian group based in Singapore called "Brightpath and Bloom". We provide expert, personalised nutrition care to support a wide range of health needs, from chronic conditions to mindful eating. Our team also offers consulting, speaking, and tailored solutions for healthcare providers, organisations, and food services.

Target Market(s)

Adults

Industry/Entity Type

Healthcare

Contact Information for Business Card

Name, position, contact number, email, website address, our logo

Requirements
Nice to have
• Clean, professional but welcoming look

```html
<!DOCTYPE html>
<html lang="en">
<head>
<meta charset="utf-8">
<title>Brightpath and Bloom – Business Card</title>
<link rel="stylesheet" href="https://fonts.googleapis.com/css2?family=Playfair+Display:wght@700&family=Tinos&display=swap">
<style>
  :root {
    --teal: #27596b;
    --paper: #ffffff;
    --ink: #3d3d3d;
    --rule: #4a4a4a;
    --stage: #e9ebec;
  }
  * { box-sizing: border-box; margin: 0; padding: 0; }
  html, body { width: 1200px; height: 1200px; overflow: hidden; }
  body {
    background: var(--stage);
    display: flex;
    flex-direction: column;
    align-items: center;
    justify-content: center;
    gap: 60px;
  }
  .card {
    position: relative;
    width: 840px;
    height: 480px;
    overflow: hidden;
    box-shadow: 0 8px 24px rgba(0,0,0,0.12);
  }
  /* Front */
  .card--front {
    background: var(--teal);
    display: flex;
    align-items: center;
    justify-content: center;
  }
  .company-name {
    font-family: "Playfair Display", serif;
    font-weight: 700;
    line-height: 1;
    white-space: nowrap;
  }
  .card--front .company-name {
    color: var(--paper);
    font-size: 62px;
    text-align: center;
  }
  /* Back */
  .card--back { background: var(--paper); }
  .card--back .company-name {
    position: absolute;
    left: 56px;
    top: 70px;
    color: var(--teal);
    font-size: 44px;
  }
  .person {
    position: absolute;
    left: 52px;
    top: 238px;
  }
  .person__name {
    font-family: "Playfair Display", serif;
    font-weight: 700;
    font-size: 40px;
    color: var(--teal);
    line-height: 1;
  }
  .person__role {
    font-family: "Tinos", serif;
    font-size: 22px;
    color: var(--ink);
    margin-top: 2px;
  }
  .divider {
    position: absolute;
    left: 44px;
    right: 54px;
    top: 318px;
    height: 1.5px;
    background: var(--rule);
  }
  .contacts {
    position: absolute;
    left: 44px;
    top: 336px;
    list-style: none;
    font-family: "Tinos", serif;
    font-size: 22px;
    color: var(--ink);
  }
  .contacts__item {
    display: flex;
    align-items: center;
    gap: 12px;
    height: 30px;
  }
  .contacts__icon {
    width: 22px;
    height: 22px;
    border-radius: 50%;
    background: var(--teal);
    display: flex;
    align-items: center;
    justify-content: center;
  }
  .address {
    position: absolute;
    right: 70px;
    top: 368px;
    font-family: "Tinos", serif;
    font-style: normal;
    font-size: 22px;
    line-height: 1.3;
    color: var(--ink);
  }
  .base-band {
    position: absolute;
    left: 0;
    right: 0;
    bottom: 0;
    height: 22px;
    background: var(--teal);
  }
</style>
</head>
<body>

  <section class="card card--front" aria-label="Card front">
    <h1 class="company-name">Brightpath and Bloom</h1>
  </section>

  <section class="card card--back" aria-label="Card back">
    <h2 class="company-name">Brightpath and Bloom</h2>

    <div class="person">
      <p class="person__name">Daniel Reyes</p>
      <p class="person__role">Managing Director</p>
    </div>

    <div class="divider"></div>

    <ul class="contacts">
      <li class="contacts__item">
        <span class="contacts__icon">
          <svg width="12" height="12" viewBox="0 0 24 24" aria-hidden="true"><path fill="#fff" d="M6.6 10.8a15 15 0 0 0 6.6 6.6l2.2-2.2c.3-.3.7-.4 1-.2 1.1.4 2.3.6 3.6.6.6 0 1 .4 1 1V20c0 .6-.4 1-1 1A17 17 0 0 1 3 4c0-.6.4-1 1-1h3.5c.6 0 1 .4 1 1 0 1.3.2 2.5.6 3.6.1.3 0 .7-.2 1z"/></svg>
        </span>
        655-210-4387
      </li>
      <li class="contacts__item">
        <span class="contacts__icon">
          <svg width="13" height="13" viewBox="0 0 24 24" aria-hidden="true"><rect x="3" y="6" width="18" height="12" fill="none" stroke="#fff" stroke-width="2"/><path d="M3 6l9 7 9-7" fill="none" stroke="#fff" stroke-width="2"/></svg>
        </span>
        hello@brightpathbloom.com
      </li>
      <li class="contacts__item">
        <span class="contacts__icon">
          <svg width="13" height="13" viewBox="0 0 24 24" aria-hidden="true"><g fill="none" stroke="#fff" stroke-width="1.8"><circle cx="12" cy="12" r="9"/><ellipse cx="12" cy="12" rx="4" ry="9"/><path d="M3 12h18"/></g></svg>
        </span>
        www.brightpathbloom.com
      </li>
    </ul>

    <address class="address">
      PO Box 214 7th Avenue<br>
      Maple Lane Singapore
    </address>

    <div class="base-band"></div>
  </section>

</body>
</html>
```